20/20 Referral Program for Optometry (Eye Doctor) Office

Hello - We looking for a flyer with a card that can be torn off at the bottom for our referral program. The flyer needs to be simple and can basically be business card on top of another with the following information. Look at the files I made a sketch of what I have in mind. We do need images that will fill in the space

Basically we are giving $20 to a person if they refer someone and then that person will receive $20 towards eyewear or an annual supply of contact lenses
http://harborlineoptics.com/2020-referral-program/

The card should have name and email of who referred them along with text that states that they will receive $20 towards the purchase of eyewear or contact lenses

http://harborlineoptics.com/wp-content/uploads/2015/02/20.20-Website-Referral-Cards.pdf

Branding look at the following files and on our website www.willowbrightvision.com

Target Market(s)

Current patients... this will be given to patients after an eye exam and they can give to a friend or family member

Industry/Entity Type

Doctor

Font styles to use
Serif
Sans Serif

Requirements
Must have
• Logo... definition of the program and a card for people to give out to friends and family. Please note this is for Willowbright Vision so use that logo. Also the barn or mountain of larkspur ski resort is nice
• Also do not use the text on Broken Glasses flyer that was for a different audience. Text can be found at the following address
• http://harborlineoptics.com/2020-referral-program/
Nice to have
• Clean look and feel. We do not need it to be text heavy we can refer to the website for Terms and Conditions
Should not have
• Up to you be creative

```html
<!DOCTYPE html>
<html lang="en">
<head>
<meta charset="utf-8">
<title>Willowbright Vision – 20/20 Referral Card</title>
<link href="https://fonts.googleapis.com/css2?family=Open+Sans:wght@400;600;700&display=swap" rel="stylesheet">
<style>
  :root {
    --bg: #e9e6e3;
    --card: #ffffff;
    --brand-red: #8b1a1f;
    --ink: #2a2a2a;
    --dots: #333333;
    --badge: #bcd9ea;
    --badge-edge: #9fc6dc;
    --flourish: #c9878a;
  }
  * { box-sizing: border-box; margin: 0; padding: 0; }
  html, body { width: 1200px; height: 844px; overflow: hidden; }
  body {
    background: var(--bg);
    font-family: "Open Sans", Arial, sans-serif;
    position: relative;
  }
  .card {
    position: absolute;
    top: 262px;
    width: 530px;
    height: 320px;
    background: var(--card);
    box-shadow: 0 6px 18px rgba(0,0,0,0.18);
    overflow: hidden;
  }

  /* Front */
  .card-front { left: 50px; }
  .brand {
    position: absolute;
    top: 44px;
    right: 44px;
    display: flex;
    align-items: center;
    gap: 10px;
  }
  .brand-mark {
    width: 14px; height: 14px;
    border-radius: 50%;
    background: var(--brand-red);
  }
  .brand-name {
    font-weight: 700;
    font-size: 28px;
    color: var(--brand-red);
    letter-spacing: 0.3px;
  }
  .doctors {
    position: absolute;
    left: 44px;
    top: 142px;
    color: var(--brand-red);
    font-weight: 600;
    font-size: 19px;
    line-height: 1.2;
  }
  .program {
    position: absolute;
    left: 44px;
    top: 206px;
    font-weight: 700;
    font-size: 15px;
    line-height: 1.35;
  }
  .program-number { color: var(--brand-red); }
  .program-name { color: var(--ink); }
  .contact {
    position: absolute;
    left: 44px;
    top: 254px;
    list-style: none;
    font-size: 16px;
    color: var(--ink);
  }
  .contact li { display: flex; align-items: center; gap: 12px; line-height: 1.6; }
  .contact svg { width: 13px; height: 13px; fill: var(--brand-red); }
  .award-badge {
    position: absolute;
    right: 40px;
    top: 178px;
    width: 66px; height: 66px;
    border-radius: 50%;
    background: var(--badge);
    border: 2px solid var(--badge-edge);
  }

  /* Back */
  .card-back { left: 620px; display: flex; flex-direction: column; }
  .band {
    background: var(--brand-red);
    color: #fff;
    text-align: center;
    font-weight: 700;
    font-size: 15px;
    flex: none;
  }
  .band-top { height: 84px; padding: 20px 50px 0; line-height: 1.35; }
  .band-bottom { height: 60px; padding-top: 16px; }
  .form-area { flex: 1; position: relative; padding: 20px 44px 0; }
  .field {
    display: flex;
    align-items: flex-end;
    color: var(--brand-red);
    font-weight: 600;
    font-size: 15px;
    height: 34px;
  }
  .field-line { flex: 1; border-bottom: 2px dotted var(--dots); margin-left: 8px; margin-bottom: 5px; }
  .field-referrer { height: 22px; }
  .field-referrer .field-label { margin-left: 130px; }
  .field-blank .field-line { margin-left: 0; }
  .flourish {
    position: absolute;
    height: 6px;
    width: 90px;
    background: linear-gradient(90deg, rgba(201,135,138,0), var(--flourish), rgba(201,135,138,0));
    border-radius: 3px;
  }
  .flourish-left { left: 14px; top: 8px; }
  .flourish-right { right: 14px; top: 8px; }
</style>
</head>
<body>
  <section class="card card-front" aria-label="Referral card front">
    <div class="brand">
      <span class="brand-mark"></span>
      <span class="brand-name">Willowbright Vision</span>
    </div>
    <div class="doctors">
      <p>Dr. Nora Whitfield</p>
      <p>Dr. Caleb Ormsby</p>
    </div>
    <div class="program">
      <p class="program-number">20/20</p>
      <p class="program-name">Referral Program</p>
    </div>
    <ul class="contact">
      <li>
        <svg viewBox="0 0 24 24" aria-hidden="true"><path d="M6.6 10.8a15.1 15.1 0 0 0 6.6 6.6l2.2-2.2a1 1 0 0 1 1-.25 11.4 11.4 0 0 0 3.6.57 1 1 0 0 1 1 1V20a1 1 0 0 1-1 1A17 17 0 0 1 3 4a1 1 0 0 1 1-1h3.5a1 1 0 0 1 1 1c0 1.25.2 2.45.57 3.57a1 1 0 0 1-.25 1z"/></svg>
        970-555-0148
      </li>
      <li>
        <svg viewBox="0 0 24 24" aria-hidden="true"><circle cx="12" cy="12" r="11"/></svg>
        www.willowbrightvision.com
      </li>
    </ul>
    <div class="award-badge" role="img" aria-label="Local award badge"></div>
  </section>

  <section class="card card-back" aria-label="Referral card back">
    <div class="band band-top">
      Present this card at your first appointment for $20 towards eye wear or contact lenses
    </div>
    <div class="form-area">
      <div class="flourish flourish-left" role="img" aria-label="Decorative flourish"></div>
      <div class="flourish flourish-right" role="img" aria-label="Decorative flourish"></div>
      <div class="field field-referrer"><span class="field-label">Referred by:</span></div>
      <div class="field field-blank"><span class="field-line"></span></div>
      <div class="field"><span class="field-label">Name :</span><span class="field-line"></span></div>
      <div class="field"><span class="field-label">Email :</span><span class="field-line"></span></div>
    </div>
    <div class="band band-bottom">We can't wait to SEE you!</div>
  </section>
</body>
</html>
```